Business Cards for new orthopaedic surgery practice

My husband and I are starting our own orthopaedic surgery practice. We are looking for a business card that is uniform, but one will have my name/title and the other will have his. You can just create one design with my name on it for now. But when I choose your design as the winning design I will ask that you add another copy with his name/title.

We are looking for classy, simple, elite all in one. We like dark blues/a little gold/yellow. Something that goes with our logo. We want our logo incorporated. Here is all the info you need:
Business name: RV Spine & Vitality Center
Location: 38915 North Bramble Ave
Maple Harbor, FL 33590
Phone: 954-218-4630
Fax: 954-571-2846
Email: info@myrvspine.example

Names: Lucinda Ferrow, M.D.
Board Certified Hand and Upper Extremity Surgeon

Emeka Dlunga, M.D.
Board Certified Hip & Knee Replacement/General Orthopaedic Surgeon

Can decide what you want to put on the back. Maybe a slogan:
Grounded in Care. Centered on You

I am just going to upload our logo. The only thing is if we select you as the winning design, the location, and phone numbers may change. We will need your help to update that once fully solidified.

Industry/Entity Type

Medical

Contact Information for Business Card

Colors
0054AA
0677BA
7BADD7
CADEEF
E8F1F8
0094D4
00A9DD
6FCCEA
C7EBF8
E9F6FB

Requirements
Must have
• class, appeal,
Should not have
• We want to air on the side of masculine if we are looking at masculine vs. feminine feel. But we still want it classy, sophisticated, and something we will love

```html
<!DOCTYPE html>
<html lang="en">
<head>
<meta charset="utf-8">
<title>RV Spine &amp; Vitality Center — Business Card</title>
<link rel="stylesheet" href="https://fonts.googleapis.com/css2?family=Cinzel:wght@600;700&family=Arimo:wght@400&family=Montserrat:wght@500&display=swap">
<style>
  :root {
    --navy: #1d2f5e;
    --navy-deep: #182650;
    --gold: #c9a45a;
    --white: #ffffff;
    --backdrop: #e4e4e4;
  }
  html, body {
    margin: 0;
    width: 1200px;
    height: 1200px;
    overflow: hidden;
    background: var(--backdrop);
  }
  .card {
    position: absolute;
    left: 265px;
    width: 690px;
    height: 394px;
    overflow: hidden;
  }
  .card--front { top: 158px; background: var(--navy); }
  .card--back { top: 652px; }
  .card__bg { position: absolute; inset: 0; }

  .brand {
    position: absolute;
    left: 30px;
    top: 150px;
    width: 270px;
    text-align: center;
    font-family: "Cinzel", serif;
    font-weight: 700;
    color: var(--navy);
    font-size: 30px;
    line-height: 1.15;
    letter-spacing: 1px;
  }
  .brand__sub { font-size: 18px; letter-spacing: 2.5px; }

  .details {
    position: absolute;
    right: 38px;
    top: 0;
    text-align: right;
    color: var(--white);
    font-family: "Arimo", sans-serif;
    font-size: 16px;
  }
  .details__name {
    position: absolute; right: 0; top: 60px; white-space: nowrap;
    font-family: "Cinzel", serif; font-weight: 700; font-size: 23px;
    color: var(--gold); letter-spacing: 0.5px;
  }
  .details__title { position: absolute; right: 0; top: 95px; width: 260px; line-height: 20px; }
  .details__address { position: absolute; right: 0; top: 210px; width: 260px; line-height: 21px; }
  .contact { position: absolute; right: 0; width: 300px; height: 20px; line-height: 20px; white-space: nowrap; }
  .contact span { margin-right: 24px; }
  .contact svg { position: absolute; right: 0; top: 3px; width: 15px; height: 15px; fill: var(--gold); }
  .contact--phone { top: 266px; }
  .contact--fax { top: 287px; }
  .contact--email { top: 308px; }
  .contact--web { top: 329px; }

  .slogan {
    position: absolute; left: 128px; top: 299px;
    font-family: "Montserrat", sans-serif; font-weight: 500;
    font-size: 15.5px; letter-spacing: 3.2px; color: var(--gold);
    white-space: nowrap;
  }
  .back-brand {
    position: absolute; right: 24px; top: 288px; text-align: center;
    font-family: "Cinzel", serif; font-weight: 700; color: var(--white);
    font-size: 12px; line-height: 1.25;
  }
</style>
</head>
<body>

<section class="card card--front" aria-label="Business card front">
  <svg class="card__bg" viewBox="0 0 690 394" width="690" height="394" aria-hidden="true">
    <defs>
      <linearGradient id="navyFade" x1="0" y1="0" x2="0" y2="1">
        <stop offset="0" stop-color="#2a3d6e"/>
        <stop offset="1" stop-color="#1b2b59"/>
      </linearGradient>
    </defs>
    <rect width="690" height="394" fill="url(#navyFade)"/>
    <circle cx="172" cy="197" r="205" fill="var(--gold)"/>
    <circle cx="161" cy="197" r="205" fill="var(--white)"/>
    <rect x="0" y="0" width="161" height="394" fill="var(--white)"/>
  </svg>

  <div class="brand">RV Spine<br><span class="brand__sub">&amp; Vitality Center</span></div>

  <div class="details">
    <div class="details__name">LUCINDA FERROW, M.D.</div>
    <div class="details__title">Board Certified Hand and<br>Upper Extremity Surgeon</div>
    <div class="details__address">38915 North Bramble Ave<br>Maple Harbor, FL 33590</div>

    <div class="contact contact--phone"><span>954-218-4630</span>
      <svg viewBox="0 0 16 16"><path d="M3.5 1l2.5 3-1.5 1.8c.8 1.8 2 3 3.8 3.9L10 8.2l3 2.5-1.3 2.8C7 13.3 2.5 8.8 1.8 3.2z"/></svg>
    </div>
    <div class="contact contact--fax"><span>954-571-2846</span>
      <svg viewBox="0 0 16 16"><rect x="4" y="1" width="8" height="5"/><rect x="1" y="7" width="14" height="7" rx="1"/></svg>
    </div>
    <div class="contact contact--email"><span>info@myrvspine.example</span>
      <svg viewBox="0 0 16 16"><path d="M1 3h14v10H1z M2 4l6 5 6-5" stroke="#1b2b59" stroke-width="1"/></svg>
    </div>
    <div class="contact contact--web"><span>www.myrvspine.example</span>
      <svg viewBox="0 0 16 16"><circle cx="8" cy="8" r="7"/><path d="M5 4c2 1 1 3 3 3s1 3 3 4" stroke="#1b2b59" stroke-width="1.4" fill="none"/></svg>
    </div>
  </div>
</section>

<section class="card card--back" aria-label="Business card back">
  <svg class="card__bg" viewBox="0 0 690 394" width="690" height="394" role="img" aria-label="Tone-on-tone repeating pattern of the practice mark across a deep navy background">
    <defs>
      <linearGradient id="backFade" x1="0" y1="0" x2="1" y2="0.4">
        <stop offset="0" stop-color="#1a2752"/>
        <stop offset="1" stop-color="#2a3f7e"/>
      </linearGradient>
    </defs>
    <rect width="690" height="394" fill="url(#backFade)"/>
  </svg>
  <div class="slogan">GROUNDED IN CARE. CENTERED ON YOU</div>
  <div class="back-brand">RV Spine<br>&amp; Vitality<br>Center</div>
</section>

</body>
</html>
```